Bright Path Attorneys Billboard Design for Personal Injury Law Firm

Need a billboard design that we can use for different versions. 1400px X 400px jpeg or png
I have attached the logo and the attorney for the billboard. Attorney Marla Benning
Here is a link to our current website brightpathlegalgroup.example

HEADLINE: HIT BY A TRUCK?
SUBHEAD: NO FEE. BIG FIGHT.
877-GRANTLY

HEADLINE: ACCIDENT?
SUBHEAD: NO FEE, UNLESS WE WIN!
877-GRANTLY

HEADLINE: BIG TRUCK. BIG CASE.
SUBHEAD: YOU PAY $0 UPFRONT
877-GRANTLY

Target Market(s)

People in Car Accident

Industry/Entity Type

Personal Injury Attorneys

```html
<!DOCTYPE html>
<html lang="en">
<head>
<meta charset="utf-8">
<title>Bright Path Attorneys – Billboard Set</title>
<link rel="stylesheet" href="https://fonts.googleapis.com/css2?family=Montserrat:wght@800&family=Oswald:wght@600&display=swap">
<style>
  :root{
    --frame:#636363;
    --board-left:#1b1f33;
    --board-right:#131418;
    --white:#ffffff;
    --green:#62b546;
    --photo-light:#c9a27a;
    --photo-dark:#1f2440;
  }
  html,body{margin:0;padding:0;overflow:hidden;}
  body{width:1200px;height:1107px;background:var(--frame);position:relative;}
  .billboard{
    position:absolute;left:15px;width:1167px;height:333px;overflow:hidden;
    background:linear-gradient(90deg,var(--board-left),var(--board-right));
  }
  .billboard--accident{top:18px;}
  .billboard--truck{top:386px;}
  .billboard--case{top:753px;}
  .attorney-photo{
    position:absolute;left:77px;top:0;width:254px;height:333px;
    background:linear-gradient(180deg,var(--photo-light) 0%,#b88d66 35%,var(--photo-dark) 70%,var(--photo-dark) 100%);
    border-radius:120px 120px 0 0;
  }
  .line{
    position:absolute;left:375px;margin:0;white-space:nowrap;line-height:1;
    font-family:"Oswald",sans-serif;font-weight:600;text-transform:uppercase;
    color:var(--white);
  }
  .line--green{color:var(--green);}
  .headline-wide{font-family:"Montserrat",sans-serif;font-weight:800;letter-spacing:-1px;}
  .rule{
    position:absolute;left:375px;width:652px;height:2px;
    background:linear-gradient(90deg,rgba(98,181,70,0) 0%,rgba(98,181,70,.85) 15%,rgba(98,181,70,.6) 80%,rgba(98,181,70,0) 100%);
  }
  .rule--light{background:linear-gradient(90deg,rgba(255,255,255,0) 0%,rgba(255,255,255,.85) 15%,rgba(255,255,255,.6) 80%,rgba(255,255,255,0) 100%);}
  .firm-name{
    position:absolute;left:900px;display:flex;align-items:center;gap:8px;
    font-family:"Oswald",sans-serif;font-weight:600;font-size:22px;line-height:1;
    color:var(--white);white-space:nowrap;letter-spacing:.5px;
  }
  .firm-name .dot{width:12px;height:12px;border-radius:50%;background:var(--green);}
</style>
</head>
<body>

<section class="billboard billboard--accident">
  <div class="attorney-photo" role="img" aria-label="Portrait of attorney Marla Benning, arms crossed, in a navy blazer"></div>
  <h1 class="line headline-wide" style="top:46px;font-size:92px;">ACCIDENT?</h1>
  <div class="rule rule--light" style="top:144px;"></div>
  <p class="line" style="top:147px;font-size:55px;">NO FEE, UNLESS WE WIN!</p>
  <div class="rule rule--light" style="top:207px;"></div>
  <p class="line line--green" style="top:218px;font-size:94px;">877-GRANTLY</p>
  <div class="firm-name" style="top:276px;"><span class="dot"></span>BRIGHT PATH ATTORNEYS</div>
</section>

<section class="billboard billboard--truck">
  <div class="attorney-photo" role="img" aria-label="Portrait of attorney Marla Benning, arms crossed, in a navy blazer"></div>
  <h1 class="line" style="top:27px;font-size:94px;">HIT BY A TRUCK?</h1>
  <div class="rule" style="top:129px;"></div>
  <p class="line line--green" style="top:124px;font-size:87px;">NO FEE. BIG FIGHT.</p>
  <div class="rule" style="top:214px;"></div>
  <p class="line" style="top:223px;font-size:82px;">877-GRANTLY</p>
  <div class="firm-name" style="top:276px;"><span class="dot"></span>BRIGHT PATH ATTORNEYS</div>
</section>

<section class="billboard billboard--case">
  <div class="attorney-photo" role="img" aria-label="Portrait of attorney Marla Benning, arms crossed, in a navy blazer"></div>
  <h1 class="line" style="top:40px;font-size:73px;">BIG TRUCK. BIG CASE.</h1>
  <div class="rule" style="top:127px;"></div>
  <p class="line line--green" style="top:123px;font-size:88px;">NO FEE. BIG FIGHT.</p>
  <div class="rule" style="top:213px;"></div>
  <p class="line" style="top:225px;font-size:80px;">877-GRANTLY</p>
  <div class="firm-name" style="top:276px;"><span class="dot"></span>BRIGHT PATH ATTORNEYS</div>
</section>

</body>
</html>
```